Breakfast Menu at a Bar and Grill

6" x 9" flyer
The attached powerpoint file contains slides with the text to be included in the front and back of the flyer. I will leave it to the designer to suggest color and background designs. Orvella's Final Wink is a no frills dive bar with a blue color customer base. A simple breakfast theme will do.

Target Market(s)

Seniors and blue collar workers.

Font styles to use
Decorative

Colors

Designer to choose colors to be used in the design.

Requirements
Must have
• Our Logo (attached jpg) and the text in the attached PowerPoint file. Some kind of breakfast dish as the background. I will rely on the designers regards the font sizes.
Nice to have
• The background design should have a pic of a breakfast plate that matches one of the items on special...perhaps two pics?
Should not have
• pic that shows food that is not listed on the flyer.

```html
<!DOCTYPE html>
<html lang="en">
<head>
<meta charset="utf-8">
<title>Orvella's Final Wink – Breakfast Specials Flyer</title>
<link href="https://fonts.googleapis.com/css2?family=Kaushan+Script&family=Pinyon+Script&family=Lato:wght@400;700;900&family=Playfair+Display:ital,wght@1,400&display=swap" rel="stylesheet">
<style>
  :root{
    --page:#ffffff;
    --sheet:#e4e4e4;
    --sheet-top:#f3f3f3;
    --ink:#111111;
    --brush:#262626;
    --orange:#f08422;
    --red:#d42a2a;
    --shadow:rgba(0,0,0,.18);
  }
  *{margin:0;padding:0;box-sizing:border-box}
  html,body{width:1200px;height:1200px;overflow:hidden;background:var(--page)}
  body{position:relative;font-family:"Lato",sans-serif;color:var(--ink)}

  .flyer{position:absolute;top:150px;width:546px;height:772px;box-shadow:0 1px 4px var(--shadow);overflow:hidden}
  .flyer--front{left:35px;background:var(--sheet)}
  .flyer--back{left:629px;width:538px}

  .front__head{position:absolute;left:0;top:0;width:100%;height:218px;background:var(--sheet-top)}
  .front__head svg{position:absolute;left:0;bottom:-14px;width:100%;height:40px}
  .title{position:absolute;left:41px;top:34px;width:470px;font-family:"Kaushan Script",cursive;font-size:51px;color:var(--orange);white-space:nowrap;line-height:1}
  .subtitle{position:absolute;left:41px;top:104px;width:270px;text-align:center;font-family:"Pinyon Script",cursive;font-size:36px;line-height:1;white-space:nowrap}
  .hours{position:absolute;left:41px;top:150px;width:250px;text-align:center;font-weight:900;font-size:25px;line-height:1}
  .days{position:absolute;left:41px;top:180px;width:250px;text-align:center;color:var(--orange);font-size:17px;line-height:1}
  .divider{position:absolute;left:322px;top:114px;width:1px;height:80px;background:#555}
  .promo{position:absolute;right:40px;top:112px;width:180px;text-align:right;font-size:11px;line-height:13.7px}

  .banner{position:absolute;height:34px}
  .banner svg{position:absolute;inset:0;width:100%;height:100%}
  .banner span{position:relative;display:block;text-align:center;font-family:"Playfair Display",serif;font-style:italic;font-size:21px;color:#fff;line-height:34px}
  .banner--favorites{left:193px;top:233px;width:322px}
  .banner--omelets{left:257px;top:405px;width:180px}
  .banner--drinks{left:231px;top:592px;width:232px}

  .menu{position:absolute;left:177px;width:330px;list-style:none}
  .menu li{display:flex;justify-content:space-between;font-size:17.5px;line-height:20.6px;text-transform:uppercase}
  .menu--favorites{top:289px;width:320px}
  .menu--omelets{top:464px;width:320px}
  .menu--drinks{top:646px;width:324px}

  .dish{position:absolute;border-radius:50%}
  .dish--pancakes{left:27px;top:286px;width:136px;height:102px;background:radial-gradient(ellipse at 50% 45%,#c98a55 0%,#a5613a 45%,#c23a2d 70%,#f2f2f2 74%)}
  .dish--omelet{left:33px;top:478px;width:140px;height:70px;border-radius:50% 50% 45% 45%;background:radial-gradient(ellipse at 40% 50%,#f5cf6a 0%,#eab748 60%,#7ab24a 80%,transparent 82%)}
  .dish--drinks{left:35px;top:640px;width:130px;height:84px;border-radius:8px;background:linear-gradient(90deg,#c94a3a,#e9a93a 40%,#b83a2c 70%,#e5c35a)}

  .back__photo{position:absolute;inset:0;background:
      radial-gradient(ellipse 50% 35% at 80% 12%,#a8243a 0%,rgba(168,36,58,0) 100%),
      radial-gradient(ellipse 55% 45% at 40% 70%,#b7283a 0%,#e9d48a 55%,rgba(233,212,138,0) 80%),
      linear-gradient(160deg,#f2ece6 0%,#ffffff 55%,#efe7e1 100%)}
  .brand{position:absolute;left:273px;top:146px;width:204px;display:flex;align-items:center;justify-content:center;gap:10px}
  .brand__dot{width:14px;height:14px;border-radius:50%;background:var(--red)}
  .brand__name{font-family:"Lato",sans-serif;font-weight:900;font-size:38px;color:var(--red);line-height:1}
  .contact{position:absolute;left:60px;top:682px;width:420px;height:50px;background:rgba(255,255,255,.75);text-align:center}
  .contact__address{font-size:16px;line-height:24px;padding-top:2px}
  .contact__phone{font-weight:900;font-size:17px;line-height:22px}
</style>
</head>
<body>

<section class="flyer flyer--front">
  <div class="front__head">
    <svg viewBox="0 0 546 40" preserveAspectRatio="none"><path d="M0 0H546V14L520 22 490 12 455 26 420 16 380 28 340 14 300 24 260 12 220 26 180 16 140 30 100 18 60 28 30 16 0 30Z" fill="var(--sheet-top)"/></svg>
  </div>
  <h1 class="title">Orvella's Final Wink</h1>
  <p class="subtitle">Breakfast Specials</p>
  <p class="hours">6AM – 11AM</p>
  <p class="days">7 Days A Week</p>
  <div class="divider"></div>
  <p class="promo">Free Breakfast on Sunday with a two drink purchase.&nbsp; Monday through Saturday; Purchase a breakfast special item with a two drink minimum and get one free.</p>

  <div class="banner banner--favorites">
    <svg viewBox="0 0 322 34" preserveAspectRatio="none"><path d="M4 3 300 5 322 6 292 12 318 16 296 22 310 30 40 32 14 30 10 22 0 17 12 12Z" fill="var(--brush)"/></svg>
    <span>Traditional Favorites</span>
  </div>
  <div class="dish dish--pancakes" role="img" aria-label="Stack of pancakes with strawberries and blueberries"></div>
  <ul class="menu menu--favorites">
    <li><span>The 5-Star Breakfast</span><span>$5.50</span></li>
    <li><span>Pancakes w/Bacon</span><span>$5.50</span></li>
    <li><span>2 Eggs Bacon or Sausage</span><span>$5.50</span></li>
    <li><span>3 Pancakes</span><span>$4.00</span></li>
    <li><span>3 French Toast</span><span>$4.00</span></li>
  </ul>

  <div class="banner banner--omelets">
    <svg viewBox="0 0 180 34" preserveAspectRatio="none"><path d="M6 2 160 4 180 6 158 13 176 19 150 26 160 32 14 32 4 24 0 16 8 9Z" fill="var(--brush)"/></svg>
    <span>Omelets</span>
  </div>
  <div class="dish dish--omelet" role="img" aria-label="Folded omelet with vegetables"></div>
  <ul class="menu menu--omelets">
    <li><span>California Omelet</span><span>$6.00</span></li>
    <li><span>Green Chili Omelet</span><span>$6.00</span></li>
    <li><span>Pueblo Omelet</span><span>$6.00</span></li>
    <li><span>Spanish Omelet</span><span>$6.00</span></li>
    <li><span>Basic Breakfast Omelet</span><span>$6.00</span></li>
  </ul>

  <div class="banner banner--drinks">
    <svg viewBox="0 0 232 34" preserveAspectRatio="none"><path d="M2 3 210 4 232 5 206 12 226 18 200 24 212 31 20 32 8 26 2 18 10 11Z" fill="var(--brush)"/></svg>
    <span>Drink Specials</span>
  </div>
  <div class="dish dish--drinks" role="img" aria-label="Assorted cocktails and beer glasses"></div>
  <ul class="menu menu--drinks">
    <li><span>Domestic Bottles</span><span>$1.75</span></li>
    <li><span>Domestic Drafts</span><span>$2.00</span></li>
    <li><span>Well Drinks</span><span>$3.00</span></li>
    <li><span>Screwdrivers</span><span>$3.00</span></li>
  </ul>
</section>

<section class="flyer flyer--back">
  <div class="back__photo" role="img" aria-label="Stack of pancakes topped with cherry sauce, berries, coconut and a mint leaf"></div>
  <div class="brand">
    <span class="brand__dot"></span>
    <span class="brand__name">Orvella's</span>
  </div>
  <div class="contact">
    <p class="contact__address">4810 N MESA RIDGE RD. | PHOENIX, AZ 85032</p>
    <p class="contact__phone">602-555-0148</p>
  </div>
</section>

</body>
</html>
```